New Website Design (Uncoded) Competition for Velto Trade Link

Please submit design concepts for a Joomla 3.0 Website for VELTO TRADE LINK company. Our client prefers a modem style design, responsive to all mobile devices,
The website demo content needs to be clear and detailed.

Menu sample:
Home/About Us/Service/Strength/Partner/News/Contact US/Blog

Requirements:
1. Only need to submit the PSD for the design, coding work is not included.
2. Please submit both Homepage and Inner page to demonstrate the concept.
3. The Homepage needs to include: LOGO/MENU/Banner/Language Switcher/Company Introduction/Welcome module/Advertising Module/Footer Menu/Footer/Copyright/Social Links
4. Use Asian business women for demo pictures/Could try city pictures for background.
5. Prefer SINGLE SCREEN design rather than scrollable multiple screen designs.
6. Avoid any chain symbol since the company is more about financial business.
7. Avoid any direct connotations related with money or cash.
Updates

Hi Designers, I have clearly state the requirements that avoid using neg connontation pictures like cash/ property, though still receive concepts like that. Please check the brief clearly and mark at Update with "cheers" Kip from LW

Target Market(s)

Shenzhen Dorvik Velto Trade link Company provide cross-border Supply chain Financial service by integrating Dorvik Trade Link resource.
The Company mission is become the most respectful, professional and valuable Chinese Supply Chain Financial Company, pioneer the supply chain industry.

Industry/Entity Type

Financial

Font styles to use
Sans Serif

Colors
33b7a4

Requirements
Must have
• 1. Necessary Web element, including Logo/navigation/ Banner/ Footer
2. Asia business Women pictures.
Should not have
• 6. Avoid any chain symbol since the company is more about financial business.

```html
<!DOCTYPE html>
<html lang="en">
<head>
<meta charset="utf-8">
<title>Velto Trade Link – About Us</title>
<link rel="stylesheet" href="https://fonts.googleapis.com/css2?family=Roboto:wght@300;400;700&display=swap">
<style>
  :root {
    --page-dim: #6e6e6e;
    --header-dim: #767676;
    --ink: #000000;
    --nav-ink: #0d0d0d;
    --nav-active: #1d5f8f;
    --muted: #3a3a3a;
    --rule: #5e5e5e;
    --panel: #ffffff;
    --photo-a: #3b2a24;
    --photo-b: #d9a48f;
  }
  * { box-sizing: border-box; margin: 0; padding: 0; }
  html, body { width: 1200px; height: 754px; overflow: hidden; }
  body {
    position: relative;
    background: var(--page-dim);
    font-family: "Roboto", Arial, sans-serif;
    color: var(--ink);
  }
  .site-header {
    position: absolute; left: 0; top: 0; width: 1200px; height: 66px;
    background: var(--header-dim);
    border-bottom: 1px solid var(--rule);
  }
  .brand {
    position: absolute; left: 160px; top: 16px;
    display: flex; align-items: center; gap: 8px;
    font-size: 17px; font-weight: 700; color: var(--nav-ink);
    letter-spacing: 0.3px;
  }
  .brand-dot { width: 28px; height: 28px; border-radius: 50%; background: #1f3f5a; }
  .main-nav {
    position: absolute; left: 380px; top: 24px;
    display: flex; gap: 18px; list-style: none;
    font-size: 14px; font-weight: 700;
  }
  .main-nav li { color: var(--nav-ink); }
  .main-nav li.is-active { color: var(--nav-active); }
  .language-switch {
    position: absolute; left: 943px; top: 26px;
    font-size: 12px; font-weight: 300; color: #2e2e2e;
    display: flex; align-items: center; gap: 4px;
  }
  .profile-modal {
    position: absolute; left: 150px; top: 67px; width: 900px; height: 629px;
    background: var(--panel);
  }
  .modal-close { position: absolute; right: 20px; top: 18px; width: 20px; height: 20px; }
  .profile-photo {
    position: absolute; left: 46px; top: 72px; width: 182px; height: 182px;
    border-radius: 50%;
    background: radial-gradient(circle at 50% 55%, var(--photo-b) 0 38%, var(--photo-a) 62%);
  }
  .profile-body { position: absolute; left: 272px; top: 70px; width: 580px; }
  .profile-name { font-size: 21px; font-weight: 700; line-height: 24px; }
  .profile-role { font-size: 17px; font-weight: 400; line-height: 20px; }
  .profile-bio p {
    font-size: 14px; line-height: 19.7px; margin-top: 19.7px;
  }
  .profile-bio p:first-child { margin-top: 23px; }
  .site-footer {
    position: absolute; left: 0; top: 695px; width: 1200px; height: 59px;
    border-top: 1px solid var(--rule);
  }
  .legal {
    position: absolute; left: 150px; top: 23px;
    font-size: 12px; font-weight: 300; color: var(--muted);
  }
  .legal a { color: var(--muted); }
  .legal .sep { margin: 0 4px; }
  .social-links { position: absolute; left: 956px; top: 20px; display: flex; gap: 16px; }
  .social-links span {
    width: 20px; height: 20px; border-radius: 50%;
    border: 1.5px solid #333;
  }
</style>
</head>
<body>
  <header class="site-header">
    <div class="brand"><span class="brand-dot"></span>VELTO TRADE LINK</div>
    <ul class="main-nav">
      <li class="is-active">ABOUT US</li>
      <li>SERVICE</li>
      <li>STRENGTH</li>
      <li>PARTNER</li>
      <li>NEWS</li>
      <li>CONTACT US</li>
      <li>BLOG</li>
    </ul>
    <div class="language-switch">Choose Language
      <svg width="9" height="6" viewBox="0 0 9 6"><path d="M1 1l3.5 3.5L8 1" fill="none" stroke="#2e2e2e" stroke-width="1.2"/></svg>
    </div>
  </header>

  <section class="profile-modal" aria-label="Team member profile">
    <svg class="modal-close" viewBox="0 0 20 20" aria-label="Close"><path d="M1 1l18 18M19 1L1 19" stroke="#000" stroke-width="2.6"/></svg>
    <div class="profile-photo" role="img" aria-label="Portrait photo of an Asian businesswoman"></div>
    <div class="profile-body">
      <h1 class="profile-name">Liora Vantessa Kemry</h1>
      <h2 class="profile-role">Partner Services</h2>
      <div class="profile-bio">
        <p>Nam imperdiet mattis orci, et auctor ex imperdiet a. Sed iaculis suscipit sagittis. In sit amet velit tempor, euismod quam eu, porta odio. Etiam ornare imperdiet justo eget vehicula. Vivamus sagittis ut augue eget pellentesque. Proin ornare non lorem pretium auctor. Nunc vehicula dapibus luctus. Cum sociis natoque penatibus et magnis dis parturient montes, nascetur ridiculus mus. Donec condimentum semper dictum. Integer eu aliquet augue. Pellentesque malesuada, sem non congue pretium, enim velit congue elit, in finibus ipsum diam in nisi. Maecenas eu ante blandit, condimentum purus eget, aliquam tortor. Sed accumsan magna eu condimentum scelerisque. Morbi in lectus ex. Class aptent taciti sociosqu ad litora torquent per conubia nostra, per inceptos himenaeos.</p>
        <p>Curabitur ultricies, tortor id tincidunt cursus, nunc enim iaculis libero, ac accumsan enim enim at diam. Ut elementum molestie nisl sed consequat. Maecenas eget purus dolor. Cras non felis egestas, pretium ante a, egestas metus. Praesent at velit ultricies, interdum lacus vitae, ullamcorper mauris. Nam nunc erat, venenatis nec leo at, bibendum dignissim magna. Cras vel auctor sapien. Vivamus sit amet purus rutrum, rutrum libero id, consectetur nulla.</p>
      </div>
    </div>
  </section>

  <footer class="site-footer">
    <div class="legal">©2014 Velto Trade Link. All Rights Reserved. <a href="#">Privacy Policy</a><span class="sep">|</span><a href="#">News</a><span class="sep">|</span><a href="#">Contact Us</a></div>
    <div class="social-links" aria-label="Social links"><span></span><span></span><span></span></div>
  </footer>
</body>
</html>
```